Q7 Landing Page

We are looking for a creative landing page & a autosignature for our email.
The launchpage will be featuring a pebbleforge provided "widget"
All instructions are in the uploaded ZIP File
**Please note that we require the landing page back complete ready to be uploaded without having to do any modifications**
Reason: Awaiting some further submissions...

```html
<!DOCTYPE html>
<html lang="en">
<head>
<meta charset="utf-8">
<title>Q7 Landing Page</title>
<link rel="stylesheet" href="https://fonts.googleapis.com/css2?family=PT+Sans+Narrow:wght@400;700&family=Lobster&display=swap">
<style>
  :root {
    --green-light: #b4cd57;
    --green-mid: #8dbb4a;
    --green-deep: #5f9f3f;
    --band-green: #3a9a2f;
    --band-dark: #1f6a1c;
    --brand-dot: #2f9e3a;
    --ink: #111111;
    --footer: #000000;
    --white: #ffffff;
    --tick: #4c9a2a;
    --field-border: #c9c9c9;
    --placeholder: #222222;
    --social: #4d7fae;
  }
  * { margin: 0; padding: 0; box-sizing: border-box; }
  html, body { width: 1200px; height: 703px; overflow: hidden; background: var(--footer); }
  .page {
    position: relative; width: 1200px; height: 703px; overflow: hidden;
    font-family: "PT Sans Narrow", "Arial Narrow", sans-serif; color: var(--ink);
  }
  .hero {
    position: absolute; left: 0; top: 0; width: 1200px; height: 600px;
    background:
      radial-gradient(ellipse 520px 380px at 700px 180px, rgba(220,235,130,0.7), transparent 70%),
      linear-gradient(90deg, var(--green-mid) 0%, var(--green-light) 45%, var(--green-mid) 80%, var(--green-deep) 100%);
  }
  .band {
    position: absolute; left: 0; top: 598px; width: 1200px; height: 14px;
    background: linear-gradient(180deg, var(--band-green) 0%, #5cbc45 45%, var(--band-dark) 100%);
  }
  .footer { position: absolute; left: 0; top: 612px; width: 1200px; height: 91px; background: var(--footer); }

  .device-art {
    position: absolute; left: 141px; top: 75px; width: 421px; height: 502px;
    border-radius: 60px;
    background:
      linear-gradient(180deg, #1b1b1b 0%, #0a0a0a 100%) 98px 3px / 248px 455px no-repeat,
      radial-gradient(ellipse 220px 260px at 50% 48%, rgba(230,120,60,0.75), rgba(200,60,140,0.35) 60%, transparent 75%);
  }

  .brand { position: absolute; left: 581px; top: 62px; display: flex; align-items: center; gap: 14px; }
  .brand-dot { width: 44px; height: 44px; border-radius: 50%; background: var(--brand-dot); flex: none; }
  .brand-name { font-weight: 700; font-size: 42px; line-height: 1; color: var(--ink); }
  .brand-tagline { position: absolute; left: 639px; top: 110px; font-size: 14px; color: var(--ink); }

  .headline { position: absolute; left: 581px; top: 155px; font-size: 28px; font-weight: 700; line-height: 1.2; }
  .lead { position: absolute; left: 581px; top: 202px; font-size: 22px; line-height: 1.2; }
  .features { position: absolute; left: 584px; top: 243px; width: 470px; list-style: none;
    display: grid; grid-template-columns: 216px 1fr; row-gap: 6px; }
  .features li { display: flex; align-items: center; gap: 8px; font-size: 22px; line-height: 26px; }
  .features svg { width: 26px; height: 24px; flex: none; }
  .cta { position: absolute; left: 581px; top: 318px; font-size: 22px; font-weight: 700; font-style: italic; line-height: 1.2; }
  .notify { position: absolute; left: 582px; top: 380px; font-family: "Lobster", cursive; font-size: 17px; line-height: 1.2; }

  .signup {
    position: absolute; left: 582px; top: 417px; width: 476px; height: 62px;
    background: var(--white); border: 1px solid var(--field-border); border-radius: 9px;
    display: flex; align-items: center; overflow: hidden;
  }
  .signup-lock {
    width: 64px; height: 100%; border-right: 1px solid var(--field-border);
    background: linear-gradient(180deg, #ffffff, #dcdcdc); display: flex; align-items: center; justify-content: center;
  }
  .signup-field {
    flex: 1; height: 100%; border: 0; outline: 0; background: transparent; padding-left: 22px;
    font-family: "PT Sans Narrow", "Arial Narrow", sans-serif; font-style: italic; font-size: 24px; color: var(--placeholder);
  }
  .signup-field::placeholder { color: var(--placeholder); opacity: 1; }

  .social { position: absolute; left: 151px; top: 636px; display: flex; align-items: center; }
  .social-label { color: var(--white); font-weight: 700; font-size: 19px; margin-right: 18px; }
  .social-links { display: flex; gap: 11px; list-style: none; }
  .social-links li { width: 22px; height: 22px; border-radius: 3px; background: var(--social); }
</style>
</head>
<body>
<main class="page">
  <section class="hero">
    <div class="device-art" role="img" aria-label="Illustration of a smartphone framed by colourful swirling floral ornaments"></div>

    <div class="brand">
      <span class="brand-dot"></span>
      <span class="brand-name">Qseven Studio</span>
    </div>
    <p class="brand-tagline">Apps that travel with your audience</p>

    <h1 class="headline">Transferring the Web into your Pocket</h1>
    <p class="lead">Instant Apps for:</p>
    <ul class="features">
      <li><svg viewBox="0 0 26 24"><path d="M2 13 L9 20 L24 3" fill="none" stroke="var(--tick)" stroke-width="4" stroke-linecap="round" stroke-linejoin="round"/></svg>Industry</li>
      <li><svg viewBox="0 0 26 24"><path d="M2 13 L9 20 L24 3" fill="none" stroke="var(--tick)" stroke-width="4" stroke-linecap="round" stroke-linejoin="round"/></svg>Viral Marketing Campaigns</li>
      <li><svg viewBox="0 0 26 24"><path d="M2 13 L9 20 L24 3" fill="none" stroke="var(--tick)" stroke-width="4" stroke-linecap="round" stroke-linejoin="round"/></svg>Product Launches</li>
    </ul>
    <p class="cta">For Mobile Solutions, come talk to us !</p>

    <p class="notify">Fill in your email address and we'll let you know when we launch</p>
    <form class="signup" action="#">
      <div class="signup-lock">
        <svg width="34" height="42" viewBox="0 0 34 42">
          <path d="M8 18 V12 a9 9 0 0 1 18 0 V18" fill="none" stroke="#8a8a8a" stroke-width="4"/>
          <rect x="3" y="18" width="28" height="22" rx="3" fill="#3a3a3a"/>
          <rect x="3" y="34" width="28" height="5" fill="#e0b020"/>
        </svg>
      </div>
      <input class="signup-field" type="email" placeholder="enter your e-mail here" aria-label="Email address">
    </form>
  </section>

  <div class="band"></div>

  <footer class="footer"></footer>
  <nav class="social" aria-label="Social links">
    <span class="social-label">Find us on</span>
    <ul class="social-links">
      <li aria-label="Social link"></li>
      <li aria-label="Social link"></li>
      <li aria-label="Social link"></li>
      <li aria-label="Social link"></li>
      <li aria-label="Social link"></li>
      <li aria-label="Social link"></li>
    </ul>
  </nav>
</main>
</body>
</html>
```